New Business Card Design Project

Make a kick ass business card for The Otter Tea Mug, using the designs. I also might like the 2nd place design logo on the back? Maybe all black with that? Not sure. Also, I'm cool with it being on metal, plastic, glass? or whatever for the business card. Maybe shaped like a shark? Let me know what else you need? Would like designs in the next day or so. Thank you.
Target Market(s)
Anyone that is cool
Contact Information for Business Card
Name: Dorian Fenwick
Phone: 317.594.8126
inventor/creator/entrepreneur/owner
www.theottertyeamug.example
social media links
https://www.facebook.com/theottertyeamug
https://twitter.com/otter_brew
https://www.instagram.com/theottertyeamug/
I'll get the Pinterest one soon
Colors
Designer to choose colors to be used in the design.
Requirements
Must have
- The Otter Tea Mug
- www.theottertyeamug.example
- social media tags?
- My logos and picture/photo of wine glass
Nice to have
- Maybe shaped like a wine glass or shark
- I'll let you decide but my same colors from my website would be nice

```html
<!DOCTYPE html>
<html lang="en">
<head>
<meta charset="utf-8">
<title>Otter Tea Mug – Business Card</title>
<link rel="stylesheet" href="https://fonts.googleapis.com/css2?family=Quicksand:wght@400&family=Montserrat:wght@700&family=Lato:wght@400&display=swap">
<style>
  :root {
    --backdrop: #2b2e33;
    --card: #1b1b1c;
    --ink: #f2f2f2;
    --ink-muted: #8d8d8d;
    --accent-red: #c8232c;
    --accent-green: #1a9a3e;
    --rule: #9b1c22;
    --photo-light: #5a5a5c;
    --photo-dark: #3a1416;
    --decor: #212122;
    --icon-phone: #d3262e;
    --icon-mail: #b0607a;
    --icon-web: #6b3448;
    --icon-insta: #1f9a43;
    --icon-face: #8dc63f;
    --icon-bird: #a01d2a;
  }
  * { box-sizing: border-box; margin: 0; padding: 0; }
  html, body { width: 1200px; height: 1000px; overflow: hidden; background: var(--backdrop); }
  .canvas { position: relative; width: 1200px; height: 1000px; }

  .card {
    position: absolute;
    left: 200px;
    width: 800px;
    height: 457px;
    border-radius: 22px;
    background: var(--card);
    overflow: hidden;
    box-shadow: 0 14px 30px rgba(0,0,0,.45);
  }
  .card--front { top: 30px; }
  .card--back { top: 513px; }

  .wordmark {
    font-family: "Quicksand", sans-serif;
    font-weight: 400;
    letter-spacing: 0.5px;
    white-space: nowrap;
  }

  /* Front */
  .card--front .wordmark {
    position: absolute;
    left: 70px;
    top: 200px;
    font-size: 46px;
    color: var(--ink);
  }
  .product-photo {
    position: absolute;
    left: 430px;
    top: 40px;
    width: 340px;
    height: 417px;
    background: linear-gradient(180deg, var(--photo-light) 0%, var(--photo-dark) 100%);
  }

  /* Back */
  .glass-decor {
    position: absolute;
    left: 110px;
    top: 70px;
    width: 170px;
    height: 320px;
    background: var(--decor);
  }
  .card--back .wordmark {
    position: absolute;
    left: 44px;
    top: 190px;
    font-size: 46px;
    color: var(--ink-muted);
  }
  .divider {
    position: absolute;
    left: 395px;
    top: 115px;
    width: 2px;
    height: 270px;
    background: var(--rule);
  }
  .contact {
    position: absolute;
    left: 418px;
    top: 112px;
  }
  .person-name {
    font-family: "Montserrat", sans-serif;
    font-weight: 700;
    font-size: 28px;
    letter-spacing: 1px;
    text-transform: uppercase;
  }
  .person-name .first { color: var(--accent-red); }
  .person-name .last { color: var(--accent-green); }
  .person-role {
    font-family: "Quicksand", sans-serif;
    font-size: 20px;
    color: var(--ink);
    margin: 2px 0 18px;
    letter-spacing: 0.5px;
  }
  .contact-list { list-style: none; }
  .contact-item {
    display: flex;
    align-items: center;
    gap: 10px;
    font-family: "Lato", sans-serif;
    font-size: 19px;
    line-height: 29px;
    color: var(--ink);
  }
  .contact-icon { width: 18px; height: 18px; flex: none; }
</style>
</head>
<body>
<div class="canvas">

  <section class="card card--front">
    <div class="wordmark">OtterTeaMug</div>
    <div class="product-photo" role="img" aria-label="Product photograph of the Otter Tea Mug"></div>
  </section>

  <section class="card card--back">
    <div class="glass-decor" role="img" aria-label="Faint product decoration"></div>
    <div class="wordmark">OtterTeaMug</div>
    <div class="divider"></div>

    <div class="contact">
      <h1 class="person-name"><span class="first">Dorian</span> <span class="last">Fenwick</span></h1>
      <p class="person-role">inventor/creator/entrepreneur/owner</p>
      <ul class="contact-list">
        <li class="contact-item">
          <svg class="contact-icon" viewBox="0 0 18 18"><circle cx="9" cy="9" r="9" fill="var(--icon-phone)"/><path d="M6 5 l2 0 l1 2.5 l-1.2 1 a5 5 0 0 0 2.2 2.2 l1-1.2 l2.5 1 l0 2 a1 1 0 0 1 -1 1 a8 8 0 0 1 -7.5 -7.5 a1 1 0 0 1 1 -1z" fill="#fff"/></svg>
          317.594.8126
        </li>
        <li class="contact-item">
          <svg class="contact-icon" viewBox="0 0 18 18"><circle cx="9" cy="9" r="9" fill="var(--icon-mail)"/><rect x="4.5" y="6" width="9" height="6.5" fill="none" stroke="#fff" stroke-width="1.2"/><path d="M4.5 6 l4.5 3.5 l4.5 -3.5" fill="none" stroke="#fff" stroke-width="1.2"/></svg>
          info@theottertyeamug.example
        </li>
        <li class="contact-item">
          <svg class="contact-icon" viewBox="0 0 18 18"><circle cx="9" cy="9" r="9" fill="var(--icon-web)"/><circle cx="9" cy="9" r="4.5" fill="none" stroke="#fff" stroke-width="1.2"/><path d="M4.5 9 h9" stroke="#fff" stroke-width="1.2"/></svg>
          www.theottertyeamug.example
        </li>
        <li class="contact-item">
          <svg class="contact-icon" viewBox="0 0 18 18"><circle cx="9" cy="9" r="9" fill="var(--icon-insta)"/></svg>
          instagram.com/theottertyeamug
        </li>
        <li class="contact-item">
          <svg class="contact-icon" viewBox="0 0 18 18"><circle cx="9" cy="9" r="9" fill="var(--icon-face)"/></svg>
          facebook.com/theottertyeamug/
        </li>
        <li class="contact-item">
          <svg class="contact-icon" viewBox="0 0 18 18"><circle cx="9" cy="9" r="9" fill="var(--icon-bird)"/></svg>
          twitter.com/otter_brew
        </li>
      </ul>
    </div>
  </section>

</div>
</body>
</html>
```